TalkBridge - Language Coaching Services

Sleek, innovative, trendy design for Language Coaching business.

TalkBridge is a new UK based company that provides Language Coaching services. We offer highly personalized on-line and face to face language courses. We also impart learning techniques workshops based on the latest neuroscience research for second-language acquisition.

Target Market(s)

Industry/Entity Type

Consulting

Contact Information for Business Card

TalkBridge
ElenaVT@talkbridge-demo.co.uk
TalkBridge-demo.co.uk
London, UK

Font styles to use
Sans Serif

```html
<!DOCTYPE html>
<html lang="en">
<head>
<meta charset="utf-8">
<title>TalkBridge – Business Card</title>
<link href="https://fonts.googleapis.com/css2?family=Lato:wght@400;700&display=swap" rel="stylesheet">
<style>
  :root {
    --page: #ecebe8;
    --card-dark: #0b0b0b;
    --card-light: #ffffff;
    --brand-blue: #1a8fc9;
    --brand-deep: #1d5f8e;
    --tick-blue: #2a86c0;
    --text-light: #f2f2f2;
    --text-grey: #7a7a7a;
    --faint: #e6ecf3;
  }
  * { margin: 0; padding: 0; box-sizing: border-box; }
  html, body { width: 1200px; height: 1000px; overflow: hidden; }
  body {
    background: var(--page);
    font-family: "Lato", Arial, sans-serif;
    position: relative;
  }
  .card {
    position: absolute;
    left: 293px;
    width: 616px;
    height: 405px;
    overflow: hidden;
    box-shadow: 0 6px 14px rgba(0,0,0,0.25);
  }
  .card--back { top: 63px; background: var(--card-dark); }
  .card--front { top: 523px; background: var(--card-light); }

  /* back */
  .back-brand {
    position: absolute;
    left: 52px; top: 184px;
    display: flex; align-items: center; gap: 10px;
  }
  .brand-dot {
    width: 16px; height: 16px; border-radius: 50%;
    background: var(--brand-blue);
  }
  .back-brand .brand-name {
    color: var(--brand-blue);
    font-size: 26px; font-weight: 700;
  }
  .services {
    position: absolute;
    left: 234px; top: 115px;
    list-style: none;
  }
  .services li {
    display: flex; align-items: center;
    height: 29.8px;
    color: var(--text-light);
    font-size: 17px;
  }
  .services svg { width: 18px; height: 16px; margin-right: 7px; }

  /* front */
  .front-mark {
    position: absolute; left: 112px; top: 43px;
    width: 92px; height: 92px; border-radius: 50%;
    border: 6px solid var(--brand-blue);
  }
  .front-brand {
    position: absolute; left: 44px; top: 136px;
    color: var(--brand-blue);
    font-size: 36px; font-weight: 700;
    letter-spacing: 1px;
  }
  .front-ring {
    position: absolute; left: 380px; top: 35px;
    width: 240px; height: 300px; border-radius: 50%;
    border: 16px solid var(--faint);
  }
  .person-name {
    position: absolute; left: 44px; top: 212px;
    color: var(--brand-blue);
    font-size: 21px; font-weight: 700;
  }
  .contacts {
    position: absolute; left: 44px; top: 254px;
    list-style: none;
  }
  .contacts li {
    display: flex; align-items: center;
    height: 29.5px;
    color: var(--text-grey);
    font-size: 17px;
  }
  .contacts svg { width: 20px; height: 18px; margin-right: 8px; }
  .band {
    position: absolute; left: 0; bottom: 0;
    width: 100%; height: 48px;
    background: linear-gradient(90deg, #0ca0dc 0%, var(--brand-blue) 45%, var(--brand-deep) 100%);
  }
</style>
</head>
<body>

<section class="card card--back">
  <div class="back-brand">
    <span class="brand-dot"></span>
    <span class="brand-name">TalkBridge</span>
  </div>
  <ul class="services">
    <li><svg viewBox="0 0 18 16"><path d="M2 9 L7 14 L16 2" fill="none" stroke="var(--tick-blue)" stroke-width="3"/></svg>Face to Face language coaching classes</li>
    <li><svg viewBox="0 0 18 16"><path d="M2 9 L7 14 L16 2" fill="none" stroke="var(--tick-blue)" stroke-width="3"/></svg>Online language coaching sessions</li>
    <li><svg viewBox="0 0 18 16"><path d="M2 9 L7 14 L16 2" fill="none" stroke="var(--tick-blue)" stroke-width="3"/></svg>Personalized Newsletters for self-learners</li>
    <li><svg viewBox="0 0 18 16"><path d="M2 9 L7 14 L16 2" fill="none" stroke="var(--tick-blue)" stroke-width="3"/></svg>Language Learning Techniques Workshops</li>
    <li><svg viewBox="0 0 18 16"><path d="M2 9 L7 14 L16 2" fill="none" stroke="var(--tick-blue)" stroke-width="3"/></svg>Mindful Learning Workshops</li>
    <li><svg viewBox="0 0 18 16"><path d="M2 9 L7 14 L16 2" fill="none" stroke="var(--tick-blue)" stroke-width="3"/></svg>Access to premium content, resources</li>
  </ul>
</section>

<section class="card card--front">
  <div class="front-ring"></div>
  <div class="front-mark"></div>
  <div class="front-brand">TALKBRIDGE</div>
  <div class="person-name">ELENA VT</div>
  <ul class="contacts">
    <li><svg viewBox="0 0 20 18"><rect x="1" y="3" width="18" height="12" fill="var(--brand-deep)"/><path d="M1 3 L10 10 L19 3" fill="none" stroke="#fff" stroke-width="1.5"/></svg>ElenaVT@talkbridge-demo.co.uk</li>
    <li><svg viewBox="0 0 20 18"><circle cx="10" cy="9" r="8" fill="none" stroke="var(--brand-deep)" stroke-width="2"/><ellipse cx="10" cy="9" rx="3.5" ry="8" fill="none" stroke="var(--brand-deep)" stroke-width="1.5"/><line x1="2" y1="9" x2="18" y2="9" stroke="var(--brand-deep)" stroke-width="1.5"/></svg>TalkBridge-demo.co.uk</li>
    <li><svg viewBox="0 0 20 18"><path d="M10 17 C5 11 4 9 4 7 A6 6 0 0 1 16 7 C16 9 15 11 10 17 Z" fill="var(--brand-deep)"/><circle cx="10" cy="7" r="2.3" fill="#fff"/></svg>London, UK</li>
  </ul>
  <div class="band"></div>
</section>

</body>
</html>
```